IT Company based on Biology Business Needs a Business Card Design

We need a business card design for a new company called 'Lumen CELL'. We develop the machine learning solutions especially focused on deep learning algorithms for biology industry. Our initial product is a vision detection on biological images to help doctors diagnose the symptoms. We would like to see designs that use the color green.

Industry/Entity Type

Business

```html
<!DOCTYPE html>
<html lang="en">
<head>
<meta charset="UTF-8">
<title>Lumen CELL — Business Card</title>
<link href="https://fonts.googleapis.com/css2?family=Open+Sans:wght@600;700&family=Lato:wght@400&display=swap" rel="stylesheet">
<style>
  :root {
    --bg: #e9e9e9;
    --card: #ffffff;
    --green: #63b53b;
    --ink: #2b2b2b;
    --rule: #bdbdbd;
  }
  * { margin: 0; padding: 0; box-sizing: border-box; }
  html, body { width: 1200px; height: 750px; overflow: hidden; }
  body { background: var(--bg); position: relative; font-family: "Lato", Arial, sans-serif; }

  .card {
    position: absolute;
    top: 218px;
    width: 492px;
    height: 281px;
    background: var(--card);
  }
  .card--front { left: 91px; }
  .card--back { left: 620px; }

  .brand {
    position: absolute;
    display: flex;
    align-items: center;
    font-family: "Open Sans", Arial, sans-serif;
    font-weight: 600;
    color: var(--green);
    letter-spacing: -1px;
    white-space: nowrap;
  }
  .brand__dot { border-radius: 50%; background: var(--green); flex: none; }

  .card--front .brand { left: 44px; top: 122px; font-size: 29px; }
  .card--front .brand__dot { width: 14px; height: 14px; margin-right: 10px; }

  .card--back .brand { left: 128px; top: 115px; font-size: 42px; }
  .card--back .brand__dot { width: 20px; height: 20px; margin-right: 14px; }

  .divider {
    position: absolute;
    left: 247px;
    top: 67px;
    width: 1px;
    height: 153px;
    background: var(--rule);
  }

  .details { position: absolute; left: 261px; top: 67px; color: var(--ink); }
  .details__name {
    font-family: "Open Sans", Arial, sans-serif;
    font-weight: 700;
    font-size: 17px;
    color: var(--green);
    line-height: 21px;
  }
  .details__role {
    font-family: "Open Sans", Arial, sans-serif;
    font-weight: 600;
    font-size: 16px;
    line-height: 21px;
    margin-bottom: 10px;
  }
  .details__address { font-size: 14px; line-height: 16px; margin-bottom: 12px; }
  .contact { list-style: none; font-size: 14px; line-height: 17px; letter-spacing: 0.3px; }
  .contact li { display: flex; align-items: center; }
  .contact svg { width: 14px; height: 14px; margin-right: 6px; flex: none; }
</style>
</head>
<body>
  <section class="card card--front">
    <div class="brand"><span class="brand__dot"></span>LUMEN CELL</div>
    <div class="divider"></div>
    <div class="details">
      <p class="details__name">Nora Kessler</p>
      <p class="details__role">Co- Founder</p>
      <p class="details__address">Po Box 47<br>Business address here</p>
      <ul class="contact">
        <li>
          <svg viewBox="0 0 14 14" aria-hidden="true"><path fill="var(--green)" d="M1 5c0-2 2-3 6-3s6 1 6 3v1h-3V4.5H4V6H1zM3 7h8l1.5 5h-11zM7 8.3a1.5 1.5 0 1 0 0 3 1.5 1.5 0 0 0 0-3z"/></svg>
          +0148270391
        </li>
        <li>
          <svg viewBox="0 0 14 14" aria-hidden="true"><rect x="1" y="3" width="12" height="8.5" fill="var(--green)"/><path d="M1.5 3.5 7 8l5.5-4.5" fill="none" stroke="#fff" stroke-width="1"/></svg>
          info@lumencell.com
        </li>
        <li>
          <svg viewBox="0 0 14 14" aria-hidden="true"><g fill="none" stroke="var(--green)" stroke-width="1.1"><circle cx="7" cy="7" r="6"/><ellipse cx="7" cy="7" rx="2.6" ry="6"/><path d="M1 7h12M2 4h10M2 10h10"/></g></svg>
          www.lumencell.com
        </li>
      </ul>
    </div>
  </section>

  <section class="card card--back">
    <div class="brand"><span class="brand__dot"></span>LUMEN CELL</div>
  </section>
</body>
</html>
```